Marketing Collaterals
Flyer, edm, web template, product label, brochure, vouchers
Hi Brondel,
Thanks for your new submissions. I like the look and feel of this set of collaterals. But as mentioned, no need to work on flyer and label.
And pls make the voucher generic so I can stamp the value of the voucher on it. Pls also make the voucher simpler and cleaner looking.
Thanks
HI Everyone,
Just to reiterate:
No need to work on flyer, product label, edm anymore.
Only need to work on the following in order of priority:
1) Website
2) Vouchers (1 generic version that I can rubber stamp value of voucher on it) pls take note of size - 148.5 mm x 70 mm
3) Brochure
Thanks.
Hi everyone,
I also noticed many of you used a lot of curves and wavy lines. I much prefer simple, clean cut straight lines. With a zen feel.
The closest to it now is probably #25.
The offer posters that I uploaded as well as the stock images should give you a clear idea of what I'm looking for.
Thanks again.
I also noticed that many of you used images that are not quite suitable. Either because they are too feminine, or contradicts the services we provide. Eg. our upper body massages are provided on chairs, so images of people lying on their back while receiving a massage may be misleading.
To make it easier for all, I have gone to Pixelharbor to look for suitable images. Here is the link to my lightbox http://www.pixelharbor-example.com/public_lightbox.mhtml?lightbox_id=48207615&code=3ac19b8e2d4470fa61c8e3907b15d2c4
Pls limit images to those in the light box instead.
Pls let me know if the link to the lightbox is not working.
Hi Everyone,
Hope you had a great start to the new year.
I am sorry for keeping all of you waiting. My business start up is going through some teething problems that prevented me from devoting time to work on the marketing collaterals. Thank you all for your patience and understanding.
And I thank the staff @ Plenvarta for allowing me to reopen this project.
To keep the project more focussed and simpler, I have decided to drop several of the items in the original scope of work, leaving only 3 items. Pls see below for update:
Items to work on in order of priority:
1)Website template
- I have uploaded an updated copy for the website
- Look and feel should be simple, clean and sophisticated
- Main colour will be black
- I have uploaded my business card, the label for the Dead Sea Salt packaging as well as 2 offer posters for your reference so you know what kind of look I am going for
2) Gift Vouchers
- Dimensions: 148.5 mm x 70 mm
- 4 colour x 1 colour
- back of the voucher will feature terms and conditions
- To save on print cost, I would like to have one single version of the voucher, with the flexibility to rubber stamp the value of the voucher. (pls let me know if this is not clear and I will be happy to clarify what I mean)
- Voucher value could include: $5 spa cash, $50 spa cash, 40 mins Foot Reflexology, 20 mins Upper Body Massage etc. These values will be rubber stamped prominently onto the generic voucher.
- Dimension: Open size - 210mm x 297mm
Closed size - 210mm x 99mm
- Brochure should follow the look and feel of the website
- Copy will need to be cut back quite a bit
Hope this provides clearer direction now.
Thank you and I look forward to seeing your work.
Hi to all designers who submitted your designs. I have been very bogged down by a series of unexpected issues on the business front. Hence have not devote time to work on this. Will look into this as soon as I can.
To staff of plenvarta, i understand I would normally have 7 days to decide but I need more time. I will come back as soon as I can.
Thanks to all for understanding.
Thanks to all designers who submitted your designs. Apologies for not getting back and providing feedback on your designs as I have been very busy with the opening of the shop.
Am looking through all of your work now. Will come back soon.
kindly send feedback on the above entries. thanks
Working on it :)
Dear Project Holder,
I saw your project.I am working on it.thanks.
Hi NimbusForgeArt,
Thank you for your submission.
Here are my comments:
#1 - As mentioned, the images of the ladies are not very appropriate and does not align with the offerings and image of the place we want to portray.
#2 - Same comments on the images of the ladies. Also, one side of the flyer should introduce Kelp Arbor and it's services and the other side is purely on the offers.
#3 - Many of images used are again not suitable as they are not part of our service offering and some of the fish therapy pictures feature the wrong type of fish.
Tip: Keep the creatives clean. Maybe better to have few but bigger appropriate pictures then to have many small pictures.
Hope the comments are helpful.
Thank you.
Hi Rovantoad,
I had every intention to award the job at the end. But if it makes it more secure, I have now guaranteed the job. I have also increased the prize money from $400 previously to $800 now.
Thanks for the feedback and hope to see your submission.
Hi all,
I need to add one more item:
Promotional pull up banner standee
It will feature the 2 promotional offers as stated in the flyer.
Also, pls note that for the A5 flyer, my preference is for it to be portrait rather than landscape.
Dear 7pixelcrafter and Brondel,
Thanks for your feedback. I have increased the prize money.
Hope to see your work soon.

```html
<!DOCTYPE html>
<html lang="en">
<head>
<meta charset="utf-8">
<title>Kelp Arbor Fish Spa – Marketing Collaterals</title>
<link href="https://fonts.googleapis.com/css2?family=Arimo:wght@400;700&display=swap" rel="stylesheet">
<style>
:root{
  --ink:#0a0f14;
  --panel:#0d1820;
  --panel-2:#102330;
  --lime:#8cc63f;
  --lime-dark:#6fa82a;
  --cyan:#29abe2;
  --blue:#0e6fa8;
  --text:#d8e3ea;
  --muted:#8fa3b1;
  --paper:#ffffff;
  --label:#333333;
}
*{box-sizing:border-box;margin:0;padding:0}
html,body{width:1200px;height:876px;overflow:hidden;background:var(--paper)}
body{font-family:"Arimo",Arial,sans-serif;color:var(--text);position:relative}
.sheet-label{position:absolute;font-size:11px;color:var(--label)}
.sheet-label.big{font-size:14px;font-weight:700}
.piece{position:absolute;background:var(--ink);overflow:hidden}
.band{position:absolute;left:0;right:0}
.band.lime{background:var(--lime)}
.band.blue{background:linear-gradient(90deg,var(--blue),var(--cyan))}
.photo{position:absolute;border-radius:2px}
.photo.water{background:linear-gradient(160deg,#3d6f86,#17384a 60%,#0d2230)}
.photo.room{background:linear-gradient(180deg,#6f8596,#2c3f4c 55%,#14222c)}
.photo.feet{background:linear-gradient(150deg,#7fb3c8,#3f7c94 50%,#20465a)}
.photo.massage{background:linear-gradient(150deg,#b99a86,#6a5a52 55%,#2b2a2c)}
.photo.tank{background:linear-gradient(180deg,#1f8fc0,#0c4f72 70%,#08293b)}
.brand{position:absolute;display:flex;align-items:center;gap:6px;color:var(--cyan);font-weight:700;white-space:nowrap}
.brand .dot{border-radius:50%;background:var(--cyan);flex:none}
.heading{position:absolute;color:var(--lime);font-weight:700}
.heading.cyan{color:var(--cyan)}
.tab{position:absolute;background:var(--lime);color:var(--ink);font-weight:700;padding:2px 6px}
.tab.blue{background:var(--cyan);color:#fff}
.copy{position:absolute;font-size:6.5px;line-height:1.45;color:var(--text)}
.copy.muted{color:var(--muted)}
.list{position:absolute;list-style:none;font-size:6.5px;line-height:1.6}
.list li::before{content:"";display:inline-block;width:4px;height:4px;background:var(--lime);margin-right:4px;vertical-align:middle}
.divider{position:absolute;top:0;bottom:0;width:1px;background:#223544}
.voucher-title{position:absolute;color:#fff;font-weight:700}
</style>
</head>
<body>

<!-- sheet labels -->
<div class="sheet-label" style="left:22px;top:4px">Inside Folder</div>
<div class="sheet-label" style="left:282px;top:4px">Back</div>
<div class="sheet-label" style="left:740px;top:4px">Front</div>
<div class="sheet-label" style="left:895px;top:4px">Flyer</div>
<div class="sheet-label" style="left:1060px;top:4px">Back</div>
<div class="sheet-label big" style="left:260px;top:456px">Brochure</div>
<div class="sheet-label" style="left:614px;top:490px">Vouchers</div>
<div class="sheet-label" style="left:614px;top:732px">Label</div>

<!-- brochure outside -->
<section class="piece brochure-outside" style="left:12px;top:19px;width:588px;height:421px">
  <div class="band lime" style="top:0;height:7px"></div>
  <div class="divider" style="left:192px"></div>
  <div class="divider" style="left:384px"></div>

  <div class="photo tank" style="left:12px;top:24px;width:110px;height:160px" role="img" aria-label="Photo of the fish spa tank"></div>
  <div class="photo room" style="left:130px;top:24px;width:52px;height:104px" role="img" aria-label="Photo of the spa interior"></div>
  <div class="photo water" style="left:12px;top:196px;width:170px;height:130px" role="img" aria-label="Photo of the reflexology lounge"></div>
  <div class="photo room" style="left:12px;top:336px;width:80px;height:70px" role="img" aria-label="Photo of the reception"></div>
  <div class="photo tank" style="left:100px;top:336px;width:82px;height:70px" role="img" aria-label="Photo of the fish pools"></div>

  <div class="brand" style="left:230px;top:170px;font-size:20px"><span class="dot" style="width:14px;height:14px"></span>Kelp Arbor</div>
  <div class="copy muted" style="left:230px;top:210px;width:140px;text-align:center;font-size:7px">12 Harbourline Crescent<br>#01-08 Harbourline Point<br>Singapore 480012<br><br>Tel: +65 6100 4827<br><br>www.kelparbor-example.com</div>

  <div class="photo feet" style="left:384px;top:7px;width:204px;height:250px" role="img" aria-label="Photo of feet in a fish spa pool"></div>
  <div class="brand" style="left:400px;top:30px;font-size:16px"><span class="dot" style="width:10px;height:10px"></span>Kelp Arbor</div>
  <div class="heading" style="left:470px;top:190px;width:110px;text-align:right;font-size:14px;line-height:1.2;color:#fff">Foot Reflexology and Fish Spa</div>
  <div class="photo water" style="left:396px;top:268px;width:180px;height:110px" role="img" aria-label="Photo of fish spa treatment"></div>
  <div class="band blue" style="bottom:0;height:34px;left:384px"></div>
</section>

<!-- flyer front -->
<section class="piece flyer-front" style="left:612px;top:19px;width:281px;height:418px;background:var(--panel)">
  <div class="band lime" style="top:0;height:8px"></div>
  <div class="brand" style="left:82px;top:26px;font-size:20px"><span class="dot" style="width:14px;height:14px"></span>Kelp Arbor</div>
  <div class="photo room" style="left:14px;top:72px;width:253px;height:190px" role="img" aria-label="Photo of the spa interior with fish tanks"></div>
  <div class="heading" style="left:14px;top:270px;width:253px;text-align:center;font-size:13px;color:#fff">Foot Reflexology and Fish Spa</div>
  <div class="tab" style="left:14px;top:292px;font-size:8px">Introduction to Kelp Arbor</div>
  <div class="copy" style="left:14px;top:312px;width:253px">Surrender your cares to the healing hands of our experienced masseurs, or be reinvigorated by the gentle nibbles of our fish. Our Experience of fish spa and more is an elegant ambience completed with leather recliners designed to promote maximum comfort, and music that soothes your senses.<br><br>It's our promise of harmonious balance for body, mind and soul.</div>
  <div class="band lime" style="bottom:0;height:10px"></div>
</section>

<!-- flyer back -->
<section class="piece flyer-back" style="left:900px;top:19px;width:288px;height:418px;background:var(--panel)">
  <div class="band lime" style="top:0;height:8px"></div>
  <div class="brand" style="left:150px;top:24px;font-size:17px"><span class="dot" style="width:12px;height:12px"></span>Kelp Arbor</div>
  <div class="tab blue" style="left:12px;top:64px;font-size:8px">Services</div>
  <div class="heading cyan" style="left:12px;top:84px;font-size:8px">Dead Sea Salt Foot Bath + Foot Reflexology</div>
  <div class="copy" style="left:12px;top:96px;width:190px">Restore balance with a warm salt soak followed by pressure point work that relieves fatigue and improves circulation throughout the body.</div>
  <div class="heading cyan" style="left:12px;top:134px;font-size:8px">Upper Body Massage</div>
  <div class="copy" style="left:12px;top:146px;width:190px">Seated massage that eases tension in the neck, shoulders and back. Ideal for a quick break during a busy day in the city.</div>
  <div class="heading cyan" style="left:12px;top:184px;font-size:8px">Fish Spa</div>
  <div class="copy" style="left:12px;top:196px;width:190px">Relax your feet in our clean pools and let the gentle fish remove dead skin, leaving your feet soft, smooth and refreshed.</div>
  <div class="photo feet" style="left:212px;top:84px;width:64px;height:44px" role="img" aria-label="Photo of a foot reflexology session"></div>
  <div class="photo massage" style="left:212px;top:134px;width:64px;height:44px" role="img" aria-label="Photo of a seated shoulder massage"></div>
  <div class="photo water" style="left:212px;top:184px;width:64px;height:44px" role="img" aria-label="Photo of fish spa pool"></div>
  <div class="tab" style="left:12px;top:246px;font-size:8px">Offer</div>
  <div class="heading" style="left:12px;top:266px;font-size:9px">1 For 1 Fish Spa Therapy</div>
  <ul class="list" style="left:12px;top:280px;width:190px"><li>Valid for 30min fish spa session</li><li>Valid Monday to Friday only</li><li>Not valid with other offers</li></ul>
  <div class="heading" style="left:12px;top:322px;font-size:9px">$10 for 10min Upper Body Massage</div>
  <ul class="list" style="left:12px;top:336px;width:190px"><li>Valid for first time customers</li><li>Valid until end of month</li></ul>
  <div class="photo feet" style="left:212px;top:266px;width:64px;height:90px" role="img" aria-label="Photo of fish nibbling feet"></div>
  <div class="copy muted" style="left:190px;top:370px;width:90px;font-size:5.5px">12 Harbourline Crescent<br>Singapore 480012<br>Tel: +65 6100 4827<br>www.kelparbor-example.com</div>
  <div class="band lime" style="bottom:0;height:10px"></div>
</section>

<!-- brochure inside -->
<section class="piece brochure-inside" style="left:12px;top:475px;width:588px;height:394px">
  <div class="band lime" style="top:0;height:10px"></div>
  <div class="divider" style="left:196px"></div>
  <div class="divider" style="left:392px"></div>

  <div class="heading" style="left:10px;top:22px;font-size:9px">A Retreat for Body &amp; Soul</div>
  <div class="copy" style="left:10px;top:36px;width:176px">Step into Kelp Arbor, your personal sanctuary for complete rejuvenation. Our calm and friendly staff are here to make every visit a pleasant one, with tea, soft music and a warm welcome.<br><br>Savour a moment of stillness as our skilled hands ease away tension and restore the natural flow of energy in your body.<br><br>Have a seat, unwind and leave the noise of the world outside. Come back often to keep body, mind and soul in harmony.</div>
  <div class="photo room" style="left:10px;top:206px;width:176px;height:160px" role="img" aria-label="Photo of the spa lounge"></div>

  <div class="tab blue" style="left:206px;top:22px;font-size:8px">SERVICES</div>
  <div class="heading" style="left:206px;top:42px;width:176px;text-align:center;font-size:9px">Foot Reflexology<br><span style="color:var(--text);font-weight:400;font-size:7px">The Way to Total Wellbeing</span></div>
  <div class="copy" style="left:206px;top:70px;width:176px">Our feet carry us through life, and pressure points on the sole connect to every organ. Reflexology gently stimulates these points to relieve stress, boost circulation and support natural healing.</div>
  <div class="photo feet" style="left:206px;top:134px;width:176px;height:100px" role="img" aria-label="Photo of foot reflexology"></div>
  <div class="heading" style="left:206px;top:244px;width:176px;text-align:center;font-size:8px">Benefits of Reflexology</div>
  <ul class="list" style="left:210px;top:258px;width:172px"><li>Reduces stress and tension</li><li>Improves blood and lymph circulation</li><li>Promotes deep relaxation</li><li>Cleanses the body of toxins</li><li>Aids digestion and sleep</li><li>Restores energy and balance</li></ul>

  <div class="heading" style="left:402px;top:22px;width:176px;text-align:center;font-size:9px">Upper Body Massage<br><span style="color:var(--text);font-weight:400;font-size:7px">Rub Those Cares Away</span></div>
  <div class="copy" style="left:402px;top:50px;width:176px">Treat yourself to a seated massage focused on the neck, shoulders and back, where daily stress tends to build up. Ideal for a short break.</div>
  <div class="photo massage" style="left:402px;top:94px;width:176px;height:90px" role="img" aria-label="Photo of seated upper body massage"></div>
  <div class="heading" style="left:402px;top:192px;width:176px;text-align:center;font-size:9px">Fish Spa<br><span style="color:var(--text);font-weight:400;font-size:7px">The Natural Pedicure</span></div>
  <div class="copy" style="left:402px;top:220px;width:176px">Experience the gentle nibbles of Garra Rufa fish as they remove dead skin and leave your feet soft, clean and refreshed.</div>
  <div class="heading" style="left:402px;top:258px;width:176px;text-align:center;font-size:8px">Benefits of Garra Rufa Fish Spa</div>
  <ul class="list" style="left:406px;top:272px;width:172px"><li>A natural exfoliation of the skin</li><li>Stimulates acupuncture points</li><li>Improves blood circulation</li><li>Relieves the body of stress</li><li>Smooth, soft and healthy feet</li></ul>
  <div class="band blue" style="bottom:0;height:10px"></div>
</section>

<!-- vouchers -->
<section class="piece voucher" style="left:612px;top:504px;width:283px;height:60px">
  <div class="band lime" style="top:0;bottom:0;left:0;width:8px"></div>
  <div class="brand" style="left:16px;top:22px;font-size:10px"><span class="dot" style="width:7px;height:7px"></span>Kelp Arbor</div>
  <div class="voucher-title" style="left:96px;top:8px;width:180px;font-size:9px;line-height:1.25">Dead Sea Salt Bath + 30min Foot Reflexology + 30min Upper Body Massage</div>
  <div class="band lime" style="bottom:0;height:5px;left:8px"></div>
</section>
<section class="piece voucher-back" style="left:900px;top:504px;width:288px;height:60px;background:var(--panel-2)">
  <div class="copy" style="left:8px;top:6px;width:272px;font-size:5.5px"><b style="color:var(--lime)">Terms and conditions:</b> Voucher is valid for one person only and must be presented upon arrival. Not exchangeable for cash. Advance booking is advised. Valid for six months from date of issue. Kelp Arbor reserves the right to amend terms.</div>
  <div class="copy muted" style="left:8px;top:44px;width:272px;font-size:5.5px">12 Harbourline Crescent, Singapore 480012 · +65 6100 4827</div>
</section>

<section class="piece voucher" style="left:612px;top:576px;width:283px;height:60px">
  <div class="band lime" style="top:0;bottom:0;left:0;width:8px"></div>
  <div class="brand" style="left:16px;top:22px;font-size:10px"><span class="dot" style="width:7px;height:7px"></span>Kelp Arbor</div>
  <div class="voucher-title" style="left:100px;top:16px;font-size:16px">30min</div>
  <div class="voucher-title" style="left:160px;top:20px;font-size:12px;color:var(--lime)">Fish Spa Therapy</div>
  <div class="band blue" style="bottom:0;height:5px;left:8px"></div>
</section>
<section class="piece voucher-back" style="left:900px;top:576px;width:288px;height:60px;background:var(--panel-2)">
  <div class="copy" style="left:8px;top:6px;width:272px;font-size:5.5px"><b style="color:var(--lime)">Terms and conditions:</b> Voucher is valid for one person only and must be presented upon arrival. Not exchangeable for cash. Advance booking is advised. Valid for six months from date of issue. Kelp Arbor reserves the right to amend terms.</div>
  <div class="copy muted" style="left:8px;top:44px;width:272px;font-size:5.5px">12 Harbourline Crescent, Singapore 480012 · +65 6100 4827</div>
</section>

<section class="piece voucher" style="left:612px;top:648px;width:283px;height:60px">
  <div class="band lime" style="top:0;bottom:0;left:0;width:8px"></div>
  <div class="brand" style="left:16px;top:22px;font-size:10px"><span class="dot" style="width:7px;height:7px"></span>Kelp Arbor</div>
  <div class="voucher-title" style="left:100px;top:10px;font-size:18px">$10 <span style="font-size:11px">voucher</span></div>
  <div class="copy" style="left:100px;top:36px;width:176px;font-size:6px">redeemable against any product or treatment at Kelp Arbor</div>
  <div class="band lime" style="bottom:0;height:5px;left:8px"></div>
</section>
<section class="piece voucher-back" style="left:900px;top:648px;width:288px;height:60px;background:var(--panel-2)">
  <div class="copy" style="left:8px;top:6px;width:272px;font-size:5.5px"><b style="color:var(--lime)">Terms and conditions:</b> Voucher is valid for one person only and must be presented upon arrival. Not exchangeable for cash. Advance booking is advised. Valid for six months from date of issue. Kelp Arbor reserves the right to amend terms.</div>
  <div class="copy muted" style="left:8px;top:44px;width:272px;font-size:5.5px">12 Harbourline Crescent, Singapore 480012 · +65 6100 4827</div>
</section>

<!-- product label -->
<section class="piece product-label" style="left:612px;top:749px;width:576px;height:120px;border:5px solid var(--lime)">
  <div class="copy" style="left:10px;top:10px;width:150px;font-size:6px"><b style="color:var(--lime)">Ingredients:</b> 100% pure Dead Sea salt, rich in natural minerals.<br><br><b style="color:var(--lime)">Directions:</b> Dissolve two spoons in warm water. Soak feet for fifteen minutes, then rinse and dry.<br><br>Net weight 500g</div>
  <div class="brand" style="left:205px;top:38px;font-size:24px"><span class="dot" style="width:16px;height:16px"></span>Kelp Arbor</div>
  <div class="heading" style="left:400px;top:22px;width:150px;text-align:center;font-size:20px;line-height:1.1">100%<br><span style="font-size:12px">DEAD SEA SALT</span></div>
  <div class="copy" style="left:400px;top:76px;width:150px;text-align:center;font-size:10px;color:var(--cyan)">Nature's miracles</div>
</section>

</body>
</html>
```